Morrow Realty Marketing Brochure

We are looking for a refresh/modern design to use on our marketing brochures...the blue paint brush stroke takes up a lot of space and isn't really speaking to us. Most of the material does not need to be reproduced...we are just looking for a clean template that we can use on all of our brochure pages, and then would like help on page 11 to make these pages look more professional.
Target Market(s)
Real Estate Developers, Small Businesses looking to lease space
Industry/Entity Type
Real Estate Development
Requirements
Nice to have
- Colors complementing the Morrow Logo

```html
<!DOCTYPE html>
<html lang="en">
<head>
<meta charset="utf-8">
<title>Morrow Realty Brochure</title>
<link href="https://fonts.googleapis.com/css2?family=Lato:wght@400;700;900&family=Montserrat:wght@600;700&display=swap" rel="stylesheet">
<style>
:root{
  --backdrop:#d4d4d6;
  --paper:#ffffff;
  --navy:#1b2a6b;
  --deep:#0f1646;
  --royal:#2f56a6;
  --sky:#9cc0e6;
  --pale:#e3eef9;
  --mist:#f3f7fb;
  --brick:#9a5a3e;
  --ink:#3a3a3a;
  --muted:#7a7f88;
  --rule:#c9ced6;
}
*{box-sizing:border-box;margin:0;padding:0}
html,body{width:1200px;height:3000px;overflow:hidden}
body{background:var(--backdrop);font-family:"Lato",sans-serif;color:var(--ink);position:relative}
.page{position:absolute;background:var(--paper);overflow:hidden;box-shadow:0 2px 6px rgba(0,0,0,.12)}
.fill{position:absolute}
.brand{display:flex;align-items:center;gap:12px;position:absolute;z-index:2;font-family:"Lato",sans-serif;font-weight:700;color:var(--navy);letter-spacing:.04em;white-space:nowrap}
.brand-mark{background:var(--royal);display:block;flex:none}
.footer-strip{position:absolute;display:flex;font-size:11px;line-height:1.45;color:var(--muted)}
.footer-strip .cell{padding:0 18px;border-left:1px solid var(--rule)}
.footer-strip .cell:first-child{border-left:none;padding-left:0}

/* Cover */
.cover{left:80px;top:60px;width:1040px;height:700px}
.cover .pattern-left{left:0;top:180px;width:280px;height:420px;background:radial-gradient(ellipse at 30% 40%,var(--sky),var(--pale) 60%,transparent 80%)}
.cover .pattern-right{right:0;top:60px;width:170px;height:260px;background:radial-gradient(ellipse at 70% 50%,#c9d9ec,transparent 70%)}
.cover .photo-mosaic{left:200px;top:40px;width:480px;height:400px;border-radius:70px;background:linear-gradient(180deg,#cfe1f3 0%,#b9d1e9 30%,#a86a4c 55%,var(--brick) 80%,#7b7470 100%)}
.title-badge{position:absolute;z-index:2;left:500px;top:30px;width:180px;height:150px;border-radius:36px;background:var(--navy);color:#fff;font-family:"Montserrat",sans-serif;font-weight:700;text-align:center;display:flex;flex-direction:column;justify-content:center;line-height:1}
.title-badge .num{font-size:46px}
.title-badge .word{font-size:24px;margin-top:4px}
.cover .brand{left:620px;top:470px;font-size:32px}
.cover .brand-mark{width:32px;height:32px}
.cover .footer-strip{left:120px;top:610px}

/* Spread */
.spread{position:absolute;left:50px;top:860px;width:1100px;height:450px;overflow:hidden;box-shadow:0 2px 6px rgba(0,0,0,.12)}
.spread .left-page{position:absolute;left:0;top:0;width:550px;height:450px;background:var(--paper);border-right:1px solid #e2e2e2;overflow:hidden}
.spread .right-page{position:absolute;left:550px;top:0;width:550px;height:450px;background:linear-gradient(180deg,var(--pale),var(--mist) 60%,#fff);overflow:hidden}
.left-page .pattern-strip{left:0;top:40px;width:180px;height:410px;background:linear-gradient(160deg,var(--sky),#c7dbef 45%,#8fa89a 75%,#eef3f7)}
.left-page .brand{left:215px;top:70px;font-size:22px}
.left-page .brand-mark{width:24px;height:24px}
.about-copy{position:absolute;left:215px;top:130px;width:300px;font-size:11.5px;line-height:1.5;text-align:justify}
.about-copy p{margin-bottom:9px}
.site-url{position:absolute;left:215px;top:405px;font-size:11px;letter-spacing:.42em;color:var(--muted)}
.team-band{position:absolute;left:0;top:26px;width:550px;height:40px;background:var(--navy);color:#fff;font-family:"Montserrat",sans-serif;font-weight:700;font-size:24px;text-align:center;line-height:40px;letter-spacing:.04em}
.team-list{position:absolute;left:30px;top:90px;width:490px;display:flex;justify-content:space-between}
.member{width:150px;text-align:center}
.member .portrait{width:112px;height:104px;margin:0 auto 8px;background:linear-gradient(180deg,#b7c6d1,#8a7a6e);border:2px solid #fff}
.member .name{font-size:10.5px;font-weight:900;color:var(--ink)}
.member .role{font-size:8.5px;color:var(--muted)}
.right-page .brand{left:40px;top:380px;font-size:20px}
.right-page .brand-mark{width:22px;height:22px}
.right-page .photo-mosaic{right:0;top:290px;width:220px;height:160px;border-radius:50px 0 0 0;background:linear-gradient(180deg,#cfe0ef,#a86a4c 50%,var(--brick) 80%,var(--royal))}

/* Perks */
.perks{left:80px;top:1410px;width:1040px;height:700px}
.perks .sky-wash{left:380px;top:0;width:660px;height:420px;background:linear-gradient(200deg,#cfe2f2,#e6f0f8 50%,transparent 80%)}
.perks-band{position:absolute;left:100px;top:50px;width:470px;height:60px;background:var(--navy);color:#fff;font-family:"Montserrat",sans-serif;font-weight:700;font-size:34px;line-height:60px;padding-left:30px;letter-spacing:.04em}
.perk-col{position:absolute;top:150px;width:260px;height:380px}
.perk-col + .perk-col{border-left:1px solid var(--rule)}
.perk{display:flex;align-items:center;gap:16px;margin:0 0 44px 30px}
.perk-tile{width:72px;height:72px;border-radius:16px;display:flex;align-items:center;justify-content:center;flex:none}
.perk-tile.navy{background:var(--navy)}
.perk-tile.royal{background:var(--royal)}
.perk-tile.grey{background:#6f737c}
.perk-tile.black{background:#23252b}
.perk-label{font-size:14px;font-weight:700;color:var(--ink)}
.perks .brand{left:110px;top:575px;font-size:42px}
.perks .brand-mark{width:40px;height:40px}
.perks .pattern-corner{right:0;bottom:0;width:400px;height:260px;background:radial-gradient(ellipse at 70% 70%,#c3d7ee,#e8f0f9 55%,transparent 80%)}

/* Back cover */
.back{left:80px;top:2210px;width:1040px;height:700px;background:linear-gradient(160deg,#2a3a86 0%,var(--navy) 35%,var(--deep) 100%)}
.back .tree-shade{left:0;top:0;width:1040px;height:300px;background:linear-gradient(180deg,rgba(60,80,150,.45),transparent)}
.back .brand{left:300px;top:400px;font-size:40px;color:#fff}
.back .brand-mark{width:38px;height:38px;background:#fff}
.back .footer-strip{left:120px;top:600px;color:#dfe5f5}
.back .footer-strip .cell{border-left-color:rgba(255,255,255,.35)}
</style>
</head>
<body>

<section class="page cover">
  <div class="fill pattern-left" role="img" aria-label="Soft blue hexagon pattern"></div>
  <div class="fill pattern-right" role="img" aria-label="Faint grey-blue hexagon pattern"></div>
  <div class="fill photo-mosaic" role="img" aria-label="Photo mosaic of the brick office building"></div>
  <div class="title-badge"><span class="num">12</span><span class="word">NORTH</span><span class="word">ELM</span></div>
  <div class="brand"><span class="brand-mark"></span>MORROW PARTNERS</div>
  <div class="footer-strip">
    <div class="cell">480 Lakeview Avenue, Suite 310<br>Fairmont Park, Illinois 60100</div>
    <div class="cell">O: 555 210 4800<br>C: 555 210 7731<br>www.morrowpartners.com</div>
    <div class="cell">Claire Benton<br>Vice President – Development Services<br>cbenton@morrowpartners.com</div>
    <div class="cell">Owen Harper<br>Senior Development Associate<br>oharper@morrowpartners.com</div>
  </div>
</section>

<section class="spread">
  <div class="left-page">
    <div class="fill pattern-strip" role="img" aria-label="Hexagon mosaic of building and greenery photos"></div>
    <div class="brand"><span class="brand-mark"></span>MORROW PARTNERS</div>
    <div class="about-copy">
      <p>Morrow Partners (Morrow) is a full-service real estate development, management and advisory company with national experience in the acquisition, development and management of commercial &amp; agricultural properties.</p>
      <p>Morrow provides build-to-suit, project management and occupancy solutions to corporations and individuals throughout North America.</p>
      <p>Morrow creates value by providing individual, professional and proven real estate development experience at a fraction of the cost of national firms. Mindful of budgets and schedules, Morrow maximizes the financial returns of projects by actively managing the real estate planning, permitting, bidding, financing and construction process.</p>
    </div>
    <div class="site-url">www.morrowpartners.com</div>
  </div>
  <div class="right-page">
    <div class="team-band">OUR TEAM</div>
    <div class="team-list">
      <div class="member"><div class="portrait" role="img" aria-label="Portrait photo of Dana Whitfield"></div><div class="name">DANA WHITFIELD</div><div class="role">President</div></div>
      <div class="member"><div class="portrait" role="img" aria-label="Portrait photo of Claire Benton"></div><div class="name">CLAIRE BENTON</div><div class="role">Vice President – Development Services</div></div>
      <div class="member"><div class="portrait" role="img" aria-label="Portrait photo of Owen Harper"></div><div class="name">OWEN HARPER</div><div class="role">Senior Development Associate</div></div>
    </div>
    <div class="fill photo-mosaic" role="img" aria-label="Hexagon mosaic of the brick building photos"></div>
    <div class="brand"><span class="brand-mark"></span>MORROW PARTNERS</div>
  </div>
</section>

<section class="page perks">
  <div class="fill sky-wash" role="img" aria-label="Faded sky and tree photo"></div>
  <div class="fill pattern-corner" role="img" aria-label="Soft blue hexagon pattern"></div>
  <div class="perks-band">LOCATION PERKS</div>

  <div class="perk-col" style="left:90px">
    <div class="perk"><div class="perk-tile black"><svg width="40" height="40" viewBox="0 0 40 40" fill="none" stroke="#fff" stroke-width="2.5" stroke-linecap="round"><circle cx="18" cy="7" r="3"/><path d="M18 12v10h9l3 8"/><circle cx="17" cy="27" r="8"/></svg></div><div class="perk-label">Wheelchair Accessible</div></div>
    <div class="perk"><div class="perk-tile navy"><svg width="40" height="40" viewBox="0 0 40 40" fill="none" stroke="#fff" stroke-width="2.5" stroke-linecap="round"><path d="M5 16a21 21 0 0 1 30 0"/><path d="M10 22a13 13 0 0 1 20 0"/><path d="M15 28a6 6 0 0 1 10 0"/><circle cx="20" cy="32" r="1.5" fill="#fff"/></svg></div><div class="perk-label">Hi-Speed Wi-Fi</div></div>
    <div class="perk"><div class="perk-tile black"><svg width="40" height="40" viewBox="0 0 40 40" fill="none" stroke="#fff" stroke-width="2.5" stroke-linecap="round" stroke-linejoin="round"><path d="M6 20L20 8l14 12"/><path d="M10 18v14h20V18"/><path d="M17 32v-8h6v8"/></svg></div><div class="perk-label">Tenant Amenities</div></div>
  </div>

  <div class="perk-col" style="left:370px">
    <div class="perk"><div class="perk-tile royal"><svg width="40" height="40" viewBox="0 0 40 40" fill="none" stroke="#fff" stroke-width="2.5" stroke-linecap="round"><circle cx="20" cy="13" r="6"/><path d="M8 34c0-7 5-11 12-11s12 4 12 11"/></svg></div><div class="perk-label">Community Manager</div></div>
    <div class="perk"><div class="perk-tile grey"><svg width="40" height="40" viewBox="0 0 40 40" fill="none" stroke="#fff" stroke-width="2.5" stroke-linecap="round"><rect x="10" y="16" width="20" height="8" rx="1"/><circle cx="8" cy="12" r="2.5"/><circle cx="32" cy="12" r="2.5"/><circle cx="8" cy="28" r="2.5"/><circle cx="32" cy="28" r="2.5"/></svg></div><div class="perk-label">Conference Rooms</div></div>
    <div class="perk"><div class="perk-tile navy"><svg width="40" height="40" viewBox="0 0 40 40" fill="none" stroke="#fff" stroke-width="2.5" stroke-linecap="round" stroke-linejoin="round"><path d="M11 5h13l6 6v24H11z"/><path d="M15 17h11M15 23h11M15 29h7"/></svg></div><div class="perk-label">Flexible Contracts</div></div>
  </div>

  <div class="perk-col" style="left:650px">
    <div class="perk"><div class="perk-tile grey"><svg width="40" height="40" viewBox="0 0 40 40" fill="none" stroke="#fff" stroke-width="2.5" stroke-linecap="round" stroke-linejoin="round"><circle cx="10" cy="26" r="6"/><circle cx="30" cy="26" r="6"/><path d="M10 26l7-11h9l4 11M17 15l3 11h-10"/></svg></div><div class="perk-label">Bike Room &amp; Showers</div></div>
    <div class="perk"><div class="perk-tile navy"><svg width="40" height="40" viewBox="0 0 40 40" fill="none" stroke="#fff" stroke-width="2.5" stroke-linecap="round"><path d="M4 24h32M8 24v10M32 24v10"/><rect x="9" y="12" width="10" height="8" rx="1"/><rect x="22" y="12" width="10" height="8" rx="1"/></svg></div><div class="perk-label">Coworking</div></div>
  </div>

  <div class="brand"><span class="brand-mark"></span>MORROW PARTNERS</div>
</section>

<section class="page back">
  <div class="fill tree-shade" role="img" aria-label="Faint tree silhouettes in navy"></div>
  <div class="brand"><span class="brand-mark"></span>MORROW PARTNERS</div>
  <div class="footer-strip">
    <div class="cell">480 Lakeview Avenue, Suite 310<br>Fairmont Park, Illinois 60100</div>
    <div class="cell">O: 555 210 4800<br>C: 555 210 7731<br>www.morrowpartners.com</div>
    <div class="cell">Claire Benton<br>Vice President – Development Services<br>cbenton@morrowpartners.com</div>
    <div class="cell">Owen Harper<br>Senior Development Associate<br>oharper@morrowpartners.com</div>
  </div>
</section>

</body>
</html>
```